Corporate Design für Anbieter von ambulanten Pflegeleistungen
Zielgruppe
Mein Unternehmen unterstützt Angehörigen und/oder Patienten mit ambulanten Pflegeleistungen, indem wir entweder zuhause (in der eigenen Häuslichkeit) oder in unseren Senioren-Wohngemeinschaften die Pflege, Betreuung und bei Bedarf auch Verköstigung der Patienten sicherstellen.
Wir kümmern uns neben den vorangegangen beschriebenen „Kernpunkten“ der Pflege (Grundpflege, Betreuungsleistungen, Verköstigung und Hauswirtschaft) ebenfalls um alle Beratungsleistungen, die im ambulanten Bereich der Pflege anfallen.
Unsere Kundschaft besteht weitestgehend aus (teils alleinstehenden) pflegebedürftigen Menschen, sowie den jeweiligen Angehörigen. Auch Menschen die Pflege an ihren Angehörigen durchführen, werden durch uns beraten.
Aufgabenstellung
Unser Firmenname lautet „Sonnwirbel GmbH“. Ein moderner Name, der eine Homage an das Wort „WanderLust“ und das mit der Pflege verbundene Gefühl der Menschlichkeit/Nächstenliebe erinnern soll.
Das Logo soll sowohl unsere Kunden (Patienten), als auch neue Fachkräfte (Recruiting) ansprechen.
Es sollte modern und einfach gehalten sein, ohne zu „dick aufzutragen“.
Es sind noch keine Farben vorgegeben, da wir diese anhand des Logo-Designs ableiten werden. Sie haben also sehr viel Freiraum, auch für die zu wählenden Schriftarten.
Der Slogan soll “Montivation Menschlichkeit” lauten.

```html
<!DOCTYPE html>
<html lang="de">
<head>
<meta charset="utf-8">
<title>Sonnwirbel GmbH – Geschäftsausstattung</title>
<link href="https://fonts.googleapis.com/css2?family=Montserrat:wght@400;500;600;700&family=Roboto:wght@300;400&display=swap" rel="stylesheet">
<style>
  :root {
    --stage: #22374f;
    --paper: #ffffff;
    --blue: #075f9e;
    --blue-bright: #0a9fd6;
    --teal: #1d9c98;
    --teal-light: #3fd0c4;
    --teal-dark: #17908c;
    --text-grey: #7a7a7a;
    --meta-grey: #8e8e8e;
  }
  * { box-sizing: border-box; margin: 0; padding: 0; }
  html, body { width: 1200px; height: 849px; overflow: hidden; }
  body { background: var(--stage); font-family: "Montserrat", sans-serif; position: relative; }

  .sheet { position: absolute; background: var(--paper); box-shadow: 0 6px 18px rgba(0,0,0,.35); overflow: hidden; }

  /* company name */
  .brand { display: flex; align-items: center; gap: 8px; }
  .brand-dot { border-radius: 50%; background: var(--teal); flex: none; }
  .brand-name { font-weight: 600; color: var(--blue); letter-spacing: .02em; line-height: 1; white-space: nowrap; }

  /* letterhead */
  .letterhead { left: 243px; top: 75px; width: 495px; height: 699px; }
  .letterhead .brand { position: absolute; left: 61px; top: 48px; }
  .letterhead .brand-dot { width: 34px; height: 34px; }
  .letterhead .brand-name { font-size: 22px; }
  .sender-line { position: absolute; left: 61px; top: 122px; font-size: 6.4px; color: var(--meta-grey); }
  .sender-line b { font-weight: 700; }
  .recipient { position: absolute; left: 61px; top: 148px; font-family: "Roboto", sans-serif; font-size: 9.6px; line-height: 11.6px; color: var(--text-grey); }
  .recipient .city { margin-top: 12px; }
  .contact-rule { position: absolute; left: 338px; top: 121px; width: 1px; height: 90px; background: #c9c9c9; }
  .contact-col { position: absolute; left: 359px; top: 121px; font-size: 6.4px; line-height: 9.2px; color: var(--meta-grey); }
  .contact-col b { font-weight: 700; }
  .contact-col p + p { margin-top: 9px; }
  .letter-body { position: absolute; left: 61px; top: 247px; width: 380px; font-family: "Roboto", sans-serif; font-size: 9.6px; line-height: 11.3px; color: var(--text-grey); }
  .letter-body p { margin-bottom: 14px; }
  .letter-body .closing { margin-top: 30px; }
  .letter-footer { position: absolute; left: 0; bottom: 0; width: 100%; height: 47px; background: linear-gradient(90deg, var(--teal-dark), var(--teal-light)); color: #fff; font-size: 6.4px; line-height: 9px; text-align: center; padding-top: 14px; padding-right: 20px; }
  .letter-accent { position: absolute; right: 0; bottom: 0; width: 120px; height: 107px; border-top-left-radius: 60px; background: linear-gradient(160deg, var(--blue), var(--blue-bright) 50%, var(--teal-light)); }

  /* business card front */
  .card-front { left: 131px; top: 292px; width: 223px; height: 144px; }
  .card-front .brand { position: absolute; left: 15px; top: 27px; gap: 5px; }
  .card-front .brand-dot { width: 16px; height: 16px; }
  .card-front .brand-name { font-size: 11px; }
  .card-person { position: absolute; right: 111px; top: 69px; text-align: right; white-space: nowrap; }
  .card-person .name { font-weight: 700; font-size: 11px; color: var(--teal); }
  .card-person .role { font-size: 6.6px; color: var(--blue); margin-top: 1px; }
  .card-person .contact { font-size: 6.4px; line-height: 9px; color: var(--blue); margin-top: 12px; }
  .card-band { position: absolute; left: 0; bottom: 0; width: 100%; height: 18px; background: linear-gradient(90deg, var(--teal-dark), var(--teal-light)); }
  .card-accent { position: absolute; right: 0; bottom: 0; width: 81px; height: 72px; border-top-left-radius: 40px; background: linear-gradient(160deg, var(--blue), var(--blue-bright) 55%, var(--teal-light)); }

  /* business card back */
  .card-back { left: 131px; top: 462px; width: 223px; height: 144px; background: linear-gradient(180deg, var(--blue-bright), var(--blue)); }
  .card-back-accent { position: absolute; left: 0; top: 0; width: 128px; height: 144px; border-top-right-radius: 70px 72px; border-bottom-right-radius: 70px 72px; background: linear-gradient(200deg, var(--blue), var(--blue-bright) 45%, var(--teal-light)); }
  .card-back .web { position: absolute; left: 138px; top: 66px; font-size: 8px; color: #fff; white-space: nowrap; }

  /* envelope */
  .envelope { left: 492px; top: 326px; width: 562px; height: 245px; }
  .envelope-band { position: absolute; left: 0; top: 0; width: 34px; height: 100%; background: linear-gradient(180deg, var(--teal-light), var(--teal-dark) 30%, var(--teal-light) 65%, var(--teal)); }
  .envelope .brand { position: absolute; left: 48px; top: 72px; }
  .envelope .brand-dot { width: 34px; height: 34px; }
  .envelope .brand-name { font-size: 22px; }
</style>
</head>
<body>

<section class="sheet letterhead" aria-label="Briefbogen">
  <div class="brand">
    <span class="brand-dot"></span>
    <span class="brand-name">SONNWIRBEL</span>
  </div>

  <p class="sender-line"><b>NAME HERE</b> Title I musterstraße 00 I 01234 Musterstadt</p>

  <div class="recipient">
    <p>Herrn</p>
    <p>Maz Mustermann</p>
    <p>musterstraße 00</p>
    <p class="city">01234 Musterstadt</p>
  </div>

  <div class="contact-rule"></div>
  <div class="contact-col">
    <p><b>NAME HERE</b><br>Title</p>
    <p>Address No. 3<br>56163</p>
    <p>08123 / 98 76 54 3<br>info@sonnwirbel.de<br>www.sonnwirbel.de</p>
  </div>

  <div class="letter-body">
    <p>Ihre Betreffzeile</p>
    <p>bezugnehmend auf den Erhalt Ihres Schreibens vom 25. November<br>möchten wir Ihnen Hinweise für das Verfassen eines Briefes geben.</p>
    <p>Beginnen Sie den Brief oben mit Ihrer Adresse und mit der Adresse<br>des Empfängers, danach folgt die Anrede. Ein Brief soll bestehen<br>aus einem einleitenden Absatz an, möglicherweise folgend<br>ein weiterer Absatz. Der letzte Absatz sollte aus einem Satz bestehen.</p>
    <p>Anbei ein Beispiel von einem Brief mit einer Bitte. Für weitere<br>Fragen stehen wir Ihnen selbstverständlich zur Verfügung.</p>
    <p class="closing">Mit freundlichen Grüßen</p>
  </div>

  <div class="letter-footer">
    Talbank Nord I IBAN: DE00 1234 5678 9000 1111 22 I BIC: TALBDEF1NRD<br>
    Steuer-Nr.: 111/222/33333 I Ust-IdNr.: DE000111222
  </div>
  <div class="letter-accent" role="img" aria-label="Dekorative Form in Blau und Türkis"></div>
</section>

<section class="sheet card-front" aria-label="Visitenkarte Vorderseite">
  <div class="brand">
    <span class="brand-dot"></span>
    <span class="brand-name">SONNWIRBEL</span>
  </div>
  <div class="card-person">
    <p class="name">Max Muster</p>
    <p class="role">MANAGER</p>
    <p class="contact">08123 / 98 76 54 3<br>info@sonnwirbel.de</p>
  </div>
  <div class="card-band"></div>
  <div class="card-accent" role="img" aria-label="Dekorative Form in Blau und Türkis"></div>
</section>

<section class="sheet card-back" aria-label="Visitenkarte Rückseite">
  <div class="card-back-accent" role="img" aria-label="Große dekorative Form in Blau und Türkis"></div>
  <p class="web">www.sonnwirbel.de</p>
</section>

<section class="sheet envelope" aria-label="Briefumschlag">
  <div class="envelope-band" role="img" aria-label="Dekorative Farbfläche in Türkis"></div>
  <div class="brand">
    <span class="brand-dot"></span>
    <span class="brand-name">SONNWIRBEL</span>
  </div>
</section>

</body>
</html>
```